Maplerise Trading Inc. needs an innovative idea for letterhead and visiting cards.

Maplerise Trading Inc. is a Canadian brand since 2007. It is a renown dealer of kids and office furniture locally. Moreover, exporting electric fixtures e.g. switches, LED's, down-lights etc. to Middle East and Africa. We have initiated a number of steps including re-branding, to boost our export in 2020. We have successfully designed our new logo a few months ago through 'Artfolio' and now we are looking for an innovative idea for a letterhead.
Some key points:
• Red, black and white are the three colors used in all our packaging and furniture. (grey is optional)
• Shouldn’t be too wide.
• Use of watermark is preferable.
• You can visit our North American site at www.mapleriseinc.com. Export website of the company will be launched soon. www.mapleriseinc.ca
• Same letterhead will be used locally and internationally.
• Our new logo and sample packaging is attached.

```html
<!DOCTYPE html>
<html lang="en">
<head>
<meta charset="utf-8">
<title>Maplerise Trading – Letterhead</title>
<link rel="stylesheet" href="https://fonts.googleapis.com/css2?family=Questrial&family=Lato:wght@400&display=swap">
<style>
  :root {
    --backdrop: #dcdcdc;
    --paper: #efefef;
    --ink-dark: #3a3a3c;
    --ink-body: #5b5b5e;
    --brand-red: #8e0a0d;
    --footer-black: #111112;
    --footer-text: #f2f2f2;
  }
  * { margin: 0; padding: 0; box-sizing: border-box; }
  html, body {
    width: 1200px;
    height: 1017px;
    overflow: hidden;
    background: var(--backdrop);
  }
  .letterhead {
    position: absolute;
    left: 230px;
    top: 28px;
    width: 740px;
    height: 961px;
    background: var(--paper);
    box-shadow: 0 6px 18px rgba(0,0,0,0.18);
    overflow: hidden;
  }
  .brand {
    position: absolute;
    left: 42px;
    top: 60px;
    display: flex;
    align-items: center;
    gap: 12px;
  }
  .brand-mark {
    width: 46px;
    height: 46px;
    background: var(--brand-red);
    border-radius: 5px;
  }
  .brand-name {
    font-family: "Questrial", sans-serif;
    font-size: 30px;
    line-height: 1;
    color: var(--ink-dark);
    letter-spacing: 0.5px;
  }
  .address {
    position: absolute;
    right: 42px;
    top: 80px;
    display: flex;
    align-items: center;
    gap: 7px;
    font-family: "Questrial", sans-serif;
    font-size: 13px;
    color: var(--ink-dark);
  }
  .address svg { width: 10px; height: 13px; }
  .letter-body {
    position: absolute;
    left: 42px;
    top: 320px;
    width: 656px;
    font-family: "Lato", sans-serif;
    font-size: 9.4px;
    line-height: 15.8px;
    color: var(--ink-body);
    text-align: justify;
  }
  .letter-body p + p { margin-top: 51px; }
  .footer-bands {
    position: absolute;
    left: 0;
    top: 0;
    width: 100%;
    height: 100%;
  }
  .contacts {
    position: absolute;
    left: 42px;
    top: 880px;
    list-style: none;
    font-family: "Questrial", sans-serif;
    font-size: 13px;
    line-height: 19.5px;
    color: var(--footer-text);
  }
  .contacts li { display: flex; align-items: center; gap: 6px; }
  .contacts svg { width: 8px; height: 8px; }
</style>
</head>
<body>
  <main class="letterhead">
    <svg class="footer-bands" viewBox="0 0 818 1063" preserveAspectRatio="none" aria-hidden="true">
      <polygon points="0,944 818,1053 818,1063 0,1063" fill="var(--footer-black)"/>
      <polygon points="505,1011 818,964 818,1053" fill="var(--brand-red)"/>
    </svg>

    <header>
      <div class="brand">
        <span class="brand-mark"></span>
        <span class="brand-name">Maplerise Trading</span>
      </div>
      <div class="address">
        <span>24 Rue des Érables, Kolwezi, DRC</span>
        <svg viewBox="0 0 10 13"><path d="M5 0a4.5 4.5 0 0 0-4.5 4.5C.5 8 5 13 5 13s4.5-5 4.5-8.5A4.5 4.5 0 0 0 5 0zm0 6.3a1.8 1.8 0 1 1 0-3.6 1.8 1.8 0 0 1 0 3.6z" fill="var(--brand-red)"/></svg>
      </div>
    </header>

    <section class="letter-body">
      <p>Lorem Ipsum is simply dummy text of the printing and typesetting industry. Lorem Ipsum has been the industry's standard dummy text ever since the 1500s, when an unknown printer took a galley of type and scrambled it to make a type specimen book. It has survived not only five centuries, but also the leap into electronic typesetting, remaining essentially unchanged. It was popularised in the 1960s with the release of transfer sheets containing Lorem Ipsum passages, and more recently with desktop publishing software like modern layout tools including versions of Lorem Ipsum.</p>
      <p>Lorem Ipsum is simply dummy text of the printing and typesetting industry. Lorem Ipsum has been the industry's standard dummy text ever since the 1500s, when an unknown printer took a galley of type and scrambled it to make a type specimen book. It has survived not only five centuries, but also the leap into electronic typesetting, remaining essentially unchanged. It was popularised in the 1960s with the release of transfer sheets containing Lorem Ipsum passages, and more recently with desktop publishing software like modern layout tools including versions of Lorem Ipsum.</p>
      <p>Lorem Ipsum is simply dummy text of the printing and typesetting industry. Lorem Ipsum has been the industry's standard dummy text ever since the 1500s, when an unknown printer took a galley of type and scrambled it to make a type specimen book. It has survived not only five centuries, but also the leap into electronic typesetting, remaining essentially unchanged. It was popularised in the 1960s with the release of transfer sheets containing Lorem Ipsum passages, and more recently with desktop publishing software like modern layout tools including versions of Lorem Ipsum.</p>
    </section>

    <ul class="contacts">
      <li>
        <svg viewBox="0 0 8 8"><path d="M1.6.3l1.2 1.5-.7.9c.4.9 1.2 1.7 2.1 2.1l.9-.7 1.5 1.2-.6 1.4C3.4 6.7 1.3 4.6.2.9z" fill="var(--brand-red)"/></svg>
        <span>+243 900 555 0147</span>
      </li>
      <li>
        <svg viewBox="0 0 8 8"><rect x="0.5" y="1.5" width="7" height="5" fill="var(--brand-red)"/><path d="M.5 1.5L4 4.3l3.5-2.8" stroke="var(--footer-black)" stroke-width=".7" fill="none"/></svg>
        <span>hello@maplerisetrading.com</span>
      </li>
      <li>
        <svg viewBox="0 0 8 8"><circle cx="4" cy="4" r="3.4" fill="none" stroke="var(--brand-red)" stroke-width="1"/><path d="M.6 4h6.8M4 .6c-1.8 2-1.8 4.8 0 6.8M4 .6c1.8 2 1.8 4.8 0 6.8" stroke="var(--brand-red)" stroke-width=".6" fill="none"/></svg>
        <span>www.maplerisetrading.com</span>
      </li>
    </ul>
  </main>
</body>
</html>
```